creation of a business card design for a company specializing in the creation...

I would like to create a design for a professional business card on a black background and with the company's colors (I am attaching some files: including the logo in horizontal and centered format, I am also attaching a recent project design a T-shirt, this is the one I chose to give you an idea of my preferences.

we are in the process of developing a new website design, it is still in the development phase but it can be viewed at the following address: www.vendrelak.be to give you other ideas about the company
you will see for yourself the subject of my main activity: company specializing in the construction of stairs

I would like a business card that stands out from the rest with a unique design

here is the informations
Name: Florent Dubrec
Function: Manager
Address: Rue Masquelin du Pont 41
7180 Val-Brunel
telephone: +32 486 219 508
email: info@rv8k.be
website: rv8k. be
social networks: Facebook, YouTube, TikTok, Instagram

Target Market(s)

customer who wants to have a beautiful staircase built

Industry/Entity Type

contruction d'escalier

Contact Information for Business Card

Adresse. Numero de telephone, site web, le texte : "Createur d'escalier", logo recto-verso, icone des reseaux sociaux

Requirements
Must have
• the mention: Stair creator
Nice to have
• an illustration of a designer staircase
Should not have
• do not distort the logo

```html
<!DOCTYPE html>
<html lang="fr">
<head>
<meta charset="utf-8">
<title>RV8K – Carte de visite</title>
<link href="https://fonts.googleapis.com/css2?family=Lato:wght@400;700&display=swap" rel="stylesheet">
<style>
  :root {
    --backdrop: #1c1c1d;
    --card: #262729;
    --edge: #6f9cbc;
    --step-light: #a9cbe2;
    --step-mid: #6e9dbf;
    --step-dark: #4f7d9f;
    --brand-blue: #5a8fb5;
    --text-light: #e6e8ea;
    --text-soft: #c9ced3;
  }
  * { margin: 0; padding: 0; box-sizing: border-box; }
  html, body { width: 1200px; height: 939px; overflow: hidden; }
  body {
    background: var(--backdrop);
    font-family: "Lato", sans-serif;
    position: relative;
  }
  .card {
    position: absolute;
    left: 280px;
    width: 640px;
    height: 400px;
    background: var(--card);
    border-radius: 22px;
    box-shadow: 0 3px 0 var(--edge);
    overflow: hidden;
  }
  .card--front { top: 46px; }
  .card--back { top: 492px; }

  .stair-illustration {
    position: absolute;
    right: 0;
    top: 0;
    width: 330px;
    height: 400px;
    background: linear-gradient(200deg, var(--step-light) 0%, var(--step-mid) 45%, var(--step-dark) 80%);
    clip-path: polygon(25% 0, 100% 0, 100% 78%, 88% 78%, 58% 45%);
  }

  .brand-name {
    position: absolute;
    color: var(--text-light);
    font-weight: 400;
    letter-spacing: 0.12em;
    line-height: 1;
  }
  .card--front .brand-name { left: 80px; top: 170px; font-size: 88px; }
  .card--back .brand-name { left: 60px; top: 70px; font-size: 54px; }

  .social-list {
    position: absolute;
    left: 150px;
    top: 292px;
    display: flex;
    gap: 8px;
    list-style: none;
  }
  .social-list li {
    width: 24px;
    height: 24px;
    border-radius: 50%;
    background: var(--brand-blue);
  }

  .person { position: absolute; left: 60px; top: 170px; }
  .person-name {
    font-size: 34px;
    font-weight: 700;
    color: var(--brand-blue);
    letter-spacing: 0.02em;
  }
  .person-role {
    font-size: 20px;
    color: var(--brand-blue);
    margin-top: 2px;
  }
  .contact-list {
    position: absolute;
    left: 60px;
    top: 268px;
    list-style: none;
    font-size: 17px;
    color: var(--text-soft);
  }
  .contact-list li {
    display: flex;
    align-items: center;
    gap: 14px;
    height: 30px;
  }
  .contact-list svg, .address svg { width: 14px; height: 14px; fill: var(--brand-blue); flex: none; }
  .address {
    position: absolute;
    left: 290px;
    top: 250px;
    display: flex;
    gap: 12px;
    font-size: 17px;
    line-height: 1.5;
    color: var(--text-soft);
  }
  .address svg { margin-top: 5px; }
</style>
</head>
<body>

  <section class="card card--front">
    <div class="stair-illustration" role="img" aria-label="Illustration d'un escalier flottant aux marches bleues"></div>
    <div class="brand-name">RV8K</div>
    <ul class="social-list" aria-label="Réseaux sociaux">
      <li></li>
      <li></li>
      <li></li>
      <li></li>
    </ul>
  </section>

  <section class="card card--back">
    <div class="stair-illustration" role="img" aria-label="Illustration d'un escalier flottant aux marches bleues"></div>
    <div class="brand-name">RV8K</div>

    <div class="person">
      <div class="person-name">FLORENT DUBREC</div>
      <div class="person-role">Créateur d'escalier</div>
    </div>

    <ul class="contact-list">
      <li>
        <svg viewBox="0 0 24 24"><path d="M6.6 10.8a15.2 15.2 0 0 0 6.6 6.6l2.2-2.2a1 1 0 0 1 1-.25 11.4 11.4 0 0 0 3.6.57 1 1 0 0 1 1 1V20a1 1 0 0 1-1 1A17 17 0 0 1 3 4a1 1 0 0 1 1-1h3.5a1 1 0 0 1 1 1c0 1.25.2 2.45.57 3.6a1 1 0 0 1-.25 1z"/></svg>
        +32 486 219 508
      </li>
      <li>
        <svg viewBox="0 0 24 24"><path d="M2 5h20v14H2z M2 5l10 8 10-8" stroke="#262729" stroke-width="1.6"/></svg>
        info@rv8k.be
      </li>
      <li>
        <svg viewBox="0 0 24 24"><circle cx="12" cy="12" r="10"/></svg>
        rv8k. be
      </li>
    </ul>

    <div class="address">
      <svg viewBox="0 0 24 24"><path d="M12 2a7 7 0 0 0-7 7c0 5 7 13 7 13s7-8 7-13a7 7 0 0 0-7-7zm0 9.5A2.5 2.5 0 1 1 12 6.5a2.5 2.5 0 0 1 0 5z"/></svg>
      <div>Rue Masquelin du Pont 41<br>7180 Val-Brunel</div>
    </div>
  </section>

</body>
</html>
```